Dorsey K. Wendell Business Card

We need a business card for our company Dorsey K. Wendell Heating & Plumbing to be distributed to potential customers. It should follow the color scheme of our logo and have a modern upscale and masculine look.

The logo is attached and the info below should also be included:

5187 W. Cedar Brook Rd.
Linden Falls, PA 17688

Russell T. Wendell
(717) 592-0817
russelltwendell@fernmail.net
dorseykwendell.net
PA #093148

Industry/Entity Type

Business

Contact Information for Business Card

5187 W. Cedar Brook Rd.
Linden Falls, PA 17688

Russell T. Wendell
(717) 592-0817
russelltwendell@fernmail.net
dorseykwendell.net
PA #093148

Colors

Designer to choose colors to be used in the design.

Requirements
Must have
• Information above included

```html
<!DOCTYPE html>
<html lang="en">
<head>
<meta charset="utf-8">
<title>Dorsey K. Wendell Business Card</title>
<link href="https://fonts.googleapis.com/css2?family=Lato:wght@400;700;900&display=swap" rel="stylesheet">
<style>
  :root {
    --blue: #2e5aa8;
    --blue-deep: #24478c;
    --blue-light: #4a78c2;
    --green: #a6d23a;
    --white: #ffffff;
    --paper: #f7f8fa;
    --ink: #2a2c33;
    --stage: #2b2c2f;
  }
  * { margin: 0; padding: 0; box-sizing: border-box; }
  html, body { width: 1200px; height: 791px; overflow: hidden; }
  body {
    background: var(--stage);
    font-family: "Lato", sans-serif;
    display: flex;
    align-items: center;
    justify-content: center;
    gap: 40px;
  }
  .card {
    position: relative;
    width: 540px;
    height: 309px;
    overflow: hidden;
    box-shadow: 0 10px 30px rgba(0,0,0,.45);
  }

  /* Front */
  .card-front {
    background: radial-gradient(ellipse at 55% 55%, var(--blue-light), var(--blue) 55%, var(--blue-deep));
  }
  .front-brand {
    position: absolute;
    top: 74px; left: 0; right: 0;
    text-align: center;
    color: var(--white);
    font-weight: 900;
    font-size: 22px;
    line-height: 1.15;
    letter-spacing: .5px;
    text-transform: uppercase;
  }
  .front-band {
    position: absolute; left: 0; right: 0;
    background: var(--green);
  }
  .front-band.upper { top: 166px; height: 9px; }
  .front-band.lower { top: 228px; height: 13px; }
  .front-web {
    position: absolute;
    top: 192px; left: 0; right: 0;
    text-align: center;
    color: var(--white);
    font-size: 15px;
    letter-spacing: .4px;
  }

  /* Back */
  .card-back { background: var(--paper); }
  .back-brand {
    position: absolute;
    top: 30px; right: 28px;
    width: 260px;
    text-align: right;
    color: var(--blue);
    font-weight: 900;
    font-size: 18px;
    line-height: 1.15;
    text-transform: uppercase;
  }
  .back-rule {
    position: absolute;
    top: 96px; left: 200px; right: 28px;
    height: 1px;
    background: var(--green);
  }
  .name-tab {
    position: absolute;
    top: 104px; left: 0;
    width: 300px; height: 44px;
    background: var(--blue);
    border: 2px solid var(--green);
    border-left: none;
    border-radius: 0 24px 24px 0;
    color: var(--white);
    font-weight: 700;
    font-size: 21px;
    line-height: 40px;
    padding-left: 22px;
  }
  .contact-list {
    position: absolute;
    top: 158px; left: 20px;
    list-style: none;
    font-size: 12.5px;
    color: var(--ink);
  }
  .contact-list li {
    display: flex; align-items: center; gap: 10px;
    height: 20px;
  }
  .contact-list svg { width: 13px; height: 13px; flex: none; }
  .contact-rule {
    position: absolute;
    top: 223px; left: 20px; right: 28px;
    height: 1px;
    background: var(--green);
  }
  .address {
    position: absolute;
    top: 230px; left: 20px;
    display: flex; gap: 10px; align-items: flex-start;
    font-size: 12.5px; line-height: 1.25;
    color: var(--ink);
  }
  .address svg { width: 13px; height: 17px; margin-top: 4px; flex: none; }
  .bottom-bar {
    position: absolute;
    left: 280px; right: 0; bottom: 0;
    height: 40px;
    background: var(--blue);
    border-top: 2px solid var(--green);
  }
  .stripes {
    position: absolute;
    left: 236px; bottom: 0;
    display: flex; gap: 4px;
  }
  .stripes span { width: 8px; height: 46px; background: var(--green); }
  .license {
    position: absolute;
    left: 0; bottom: 0;
    width: 228px; height: 34px;
    background: var(--blue);
    border-top: 2px solid var(--green);
    color: var(--white);
    font-size: 18px;
    line-height: 32px;
    padding-left: 18px;
    letter-spacing: .5px;
  }
</style>
</head>
<body>
  <section class="card card-front">
    <div class="front-brand">Dorsey K. Wendell<br>Heating &amp; Plumbing</div>
    <div class="front-band upper"></div>
    <div class="front-web">www.dorseykwendell.net</div>
    <div class="front-band lower"></div>
  </section>

  <section class="card card-back">
    <div class="back-brand">Dorsey K. Wendell<br>Heating &amp; Plumbing</div>
    <div class="back-rule"></div>
    <div class="name-tab">Russell T. Wendell</div>
    <ul class="contact-list">
      <li>
        <svg viewBox="0 0 13 13" aria-hidden="true"><rect x="3" y="0.5" width="7" height="12" rx="1.5" fill="none" stroke="#a6d23a" stroke-width="1.3"/><circle cx="6.5" cy="10.3" r=".8" fill="#a6d23a"/></svg>
        (717) 592-0817
      </li>
      <li>
        <svg viewBox="0 0 13 13" aria-hidden="true"><rect x=".5" y="2.5" width="12" height="8" fill="#a6d23a"/><path d="M.5 2.5l6 4.5 6-4.5" fill="none" stroke="#fff" stroke-width="1"/></svg>
        russelltwendell@fernmail.net
      </li>
      <li>
        <svg viewBox="0 0 13 13" aria-hidden="true"><circle cx="6.5" cy="6.5" r="6" fill="#a6d23a"/><path d="M.5 6.5h12M6.5.5c-3 3-3 9 0 12M6.5.5c3 3 3 9 0 12" fill="none" stroke="#fff" stroke-width=".9"/></svg>
        www.dorseykwendell.net
      </li>
    </ul>
    <div class="contact-rule"></div>
    <div class="address">
      <svg viewBox="0 0 13 17" aria-hidden="true"><path d="M6.5 16S1 9.5 1 6a5.5 5.5 0 0 1 11 0c0 3.5-5.5 10-5.5 10z" fill="#2e5aa8"/><circle cx="6.5" cy="6" r="2" fill="#fff"/></svg>
      <span>5187 W. Cedar Brook Rd.<br>Linden Falls, PA 17688</span>
    </div>
    <div class="bottom-bar"></div>
    <div class="stripes"><span></span><span></span><span></span></div>
    <div class="license">PA #093148</div>
  </section>
</body>
</html>
```